New Business Card Design Project

We are looking for a talented individual to create a truly awesome/unique business card design for us. We are looking for a someone to design something that will really stand out from the crowd - we don't mind what ideas you come up with (ie embossed/flat/matte/shine etc etc) just wow us with your creativity.
Updates

Target Market(s)

Video Games Industry Professionals (all levels of seniority from QA Testers through to CEOs)

Contact Information for Business Card

Company logo (see upload)
Company name: Northbay Play Careers Ltd
Employee Name: Darren Elsby
Job title: CEO
Website: www.nbpc2go.example
Office +44 1632 960418
Mobile: +44 7700 900276
Email: darren@nbpc2go.example

Colors

Designer to choose colors to be used in the design.

Requirements
Must have
• The business card design MUST contain all the information listed in the BUSINESS CARD DETAILS box.
• You will see the colours that are relevant to us (ie company logo) in the uploaded imagery - however you do not have to use all these colours when designing the business card itself
• MUST BE DOUBLE SIDED

```html
<!DOCTYPE html>
<html lang="en">
<head>
<meta charset="utf-8">
<title>Northbay Play Careers – Business Card</title>
<link rel="stylesheet" href="https://fonts.googleapis.com/css2?family=Fira+Sans+Condensed:wght@500;600;700&family=Barlow:wght@400;500&display=swap">
<style>
  :root {
    --page-bg: #ffffff;
    --card-bg: #000000;
    --ink: #ffffff;
    --accent: #f07f0a;
    --brand-mark: #2b3170;
  }
  * { box-sizing: border-box; margin: 0; padding: 0; }
  html, body {
    width: 1200px; height: 1200px; overflow: hidden;
    background: var(--page-bg);
  }
  .canvas { position: relative; width: 1200px; height: 1200px; }
  .card {
    position: absolute; left: 110px; top: 301px;
    width: 980px; height: 598px;
    background: var(--card-bg); color: var(--ink);
  }
  .brand {
    position: absolute; left: 537px; top: 55px;
    display: flex; align-items: center; gap: 18px;
  }
  .brand-dot {
    width: 96px; height: 96px; border-radius: 50%;
    background: var(--brand-mark);
  }
  .brand-name {
    font-family: "Fira Sans Condensed", sans-serif;
    font-weight: 700; font-size: 31px; line-height: 31px;
    color: var(--ink);
  }
  .person { position: absolute; left: 74px; top: 294px; }
  .person-name {
    font-family: "Fira Sans Condensed", sans-serif;
    font-weight: 600; font-size: 50px; line-height: 54px;
    letter-spacing: -0.5px;
  }
  .person-title {
    font-family: "Fira Sans Condensed", sans-serif;
    font-weight: 600; font-size: 31px; line-height: 34px;
    margin-left: 3px;
  }
  .divider {
    position: absolute; left: 55px; top: 405px;
    width: 870px; height: 3px; background: var(--ink);
  }
  .contacts {
    position: absolute; left: 75px; top: 438px;
    display: grid; grid-template-columns: 340px 420px;
    row-gap: 20px;
  }
  .contact { display: flex; align-items: center; gap: 14px; height: 54px; }
  .contact-icon { width: 54px; height: 54px; flex: none; }
  .contact-text {
    font-family: "Barlow", sans-serif; font-weight: 400;
    font-size: 22px; letter-spacing: 0.5px; white-space: nowrap;
  }
</style>
</head>
<body>
<div class="canvas">
  <section class="card">
    <div class="brand">
      <div class="brand-dot"></div>
      <div class="brand-name">Northbay Play<br>Careers</div>
    </div>

    <div class="person">
      <h1 class="person-name">Darren Elsby</h1>
      <p class="person-title">CEO</p>
    </div>

    <div class="divider"></div>

    <div class="contacts">
      <div class="contact">
        <svg class="contact-icon" viewBox="0 0 54 54" aria-hidden="true">
          <circle cx="27" cy="27" r="27" fill="var(--accent)"/>
          <g fill="none" stroke="#fff" stroke-width="2">
            <circle cx="27" cy="27" r="15"/>
            <ellipse cx="27" cy="27" rx="7" ry="15"/>
            <line x1="27" y1="12" x2="27" y2="42"/>
            <line x1="12" y1="27" x2="42" y2="27"/>
            <path d="M14 20 H40 M14 34 H40"/>
          </g>
        </svg>
        <span class="contact-text">www.nbpc2go.example</span>
      </div>
      <div class="contact">
        <svg class="contact-icon" viewBox="0 0 54 54" aria-hidden="true">
          <circle cx="27" cy="27" r="27" fill="var(--accent)"/>
          <rect x="18" y="11" width="18" height="32" rx="3" fill="none" stroke="#fff" stroke-width="3"/>
          <rect x="24" y="38" width="6" height="2" fill="#fff"/>
        </svg>
        <span class="contact-text">+44 7700 900276</span>
      </div>
      <div class="contact">
        <svg class="contact-icon" viewBox="0 0 54 54" aria-hidden="true">
          <circle cx="27" cy="27" r="27" fill="var(--accent)"/>
          <path d="M27 30 C22 24 21 22 21 19 A6 6 0 0 1 33 19 C33 22 32 24 27 30 Z" fill="none" stroke="#fff" stroke-width="2.5"/>
          <circle cx="27" cy="19" r="2" fill="#fff"/>
          <path d="M18 32 L14 40 H40 L36 32" fill="none" stroke="#fff" stroke-width="2.5" stroke-linejoin="round"/>
        </svg>
        <span class="contact-text">+44 1632 960418</span>
      </div>
      <div class="contact">
        <svg class="contact-icon" viewBox="0 0 54 54" aria-hidden="true">
          <circle cx="27" cy="27" r="27" fill="var(--accent)"/>
          <rect x="13" y="17" width="28" height="20" rx="2" fill="#fff"/>
          <path d="M13 19 L27 29 L41 19" fill="none" stroke="var(--accent)" stroke-width="2.5"/>
        </svg>
        <span class="contact-text">darren@nbpc2go.example</span>
      </div>
    </div>
  </section>
</div>
</body>
</html>
```